Label Design for a Small Batch Liqueur

Need a label designed for a small batch South African liqueur known as Ter Sloek, that will be given to clients as a gift from our family owned company.

Ter Sloek is produced using brandy that is then infused with naartjies (a type of mandarin) and a selection of spices. Ter Sloek was traditionally produced in the Cape winelands in South Africa, and is supposedly named after Admiral Ter Sloek of the Nordic-West Isles Merchant company, who drank it to distraction.

The label will be placed on bottles 154mm tall and 73mm wide. More details are contained in the following link http://www.tallorvex.com.au/category/product/cat1/Beverage/cat2/Spirit/cat3/Glass/total/47/page/1/code/QX-311-5520-TB

The label must include our family surname, Kemp, as well as the liqueur name, Ter Sloek, and must have some allusion to it's South African heritage.

It Company

```html
<!DOCTYPE html>
<html lang="en">
<head>
<meta charset="utf-8">
<title>Ter Sloek Liqueur Label</title>
<link rel="stylesheet" href="https://fonts.googleapis.com/css2?family=Cormorant+Garamond:wght@500&family=Marcellus&family=Nothing+You+Could+Do&display=swap">
<style>
  :root {
    --backdrop: #e9eaec;
    --label-black: #0b0b0b;
    --frame-grey: #8d8d8d;
    --title-white: #ffffff;
    --accent-gold: #c9b53c;
    --map-tone: #1c1c1c;
    --map-glow: #2a2610;
  }
  html, body {
    margin: 0;
    padding: 0;
    width: 770px;
    height: 1200px;
    overflow: hidden;
    background: var(--backdrop);
  }
  .canvas {
    position: relative;
    width: 770px;
    height: 1200px;
  }
  .label {
    position: absolute;
    left: 94px;
    top: 148px;
    width: 581px;
    height: 903px;
    background: var(--label-black);
    box-shadow: 0 4px 18px rgba(0,0,0,0.18);
  }
  .label-frame {
    position: absolute;
    inset: 6px;
    border: 2px solid var(--frame-grey);
    outline: 1px solid var(--frame-grey);
    outline-offset: 3px;
    pointer-events: none;
  }
  .rule {
    position: absolute;
    left: 34px;
    width: 511px;
    height: 7px;
    background: var(--title-white);
  }
  .rule--top { top: 116px; }
  .rule--bottom { top: 273px; }
  .product-name {
    position: absolute;
    left: 0;
    width: 100%;
    top: 136px;
    margin: 0;
    text-align: center;
    font-family: "Cormorant Garamond", serif;
    font-weight: 500;
    font-size: 104px;
    line-height: 120px;
    color: var(--title-white);
    letter-spacing: -0.01em;
    transform: scaleX(0.92);
  }
  .category {
    position: absolute;
    left: 0;
    width: 100%;
    top: 316px;
    margin: 0;
    text-align: center;
    font-family: "Marcellus", serif;
    font-size: 34px;
    line-height: 40px;
    letter-spacing: 0.62em;
    text-indent: 0.62em;
    color: var(--accent-gold);
  }
  .heritage-map {
    position: absolute;
    left: 108px;
    top: 378px;
    width: 381px;
    height: 420px;
    display: block;
  }
  .family-name {
    position: absolute;
    left: 0;
    width: 100%;
    top: 388px;
    margin: 0;
    text-align: center;
    font-family: "Nothing You Could Do", cursive;
    font-size: 110px;
    line-height: 150px;
    color: var(--accent-gold);
  }
  .infusion {
    position: absolute;
    left: 0;
    width: 100%;
    top: 596px;
    margin: 0;
    text-align: center;
    font-family: "Marcellus", serif;
    font-size: 22px;
    line-height: 37.5px;
    letter-spacing: 0.36em;
    text-indent: 0.36em;
    color: var(--accent-gold);
  }
  .volume {
    position: absolute;
    left: 0;
    width: 100%;
    top: 828px;
    margin: 0;
    text-align: center;
    font-family: "Cormorant Garamond", serif;
    font-weight: 500;
    font-size: 28px;
    line-height: 32px;
    color: var(--title-white);
  }
</style>
</head>
<body>
  <main class="canvas">
    <section class="label">
      <div class="label-frame"></div>
      <div class="rule rule--top"></div>
      <h1 class="product-name">TER SLOEK</h1>
      <div class="rule rule--bottom"></div>
      <p class="category">LIQUEUR</p>
      <svg class="heritage-map" viewBox="0 0 381 420" role="img" aria-label="Outline map of Africa with South Africa highlighted in gold">
        <defs>
          <radialGradient id="map-fill" cx="55%" cy="80%" r="70%">
            <stop offset="0%" stop-color="var(--map-glow)"/>
            <stop offset="100%" stop-color="var(--map-tone)"/>
          </radialGradient>
        </defs>
        <rect x="0" y="0" width="381" height="420" rx="40" fill="url(#map-fill)" opacity="0.7"/>
      </svg>
      <p class="family-name">Kemp</p>
      <p class="infusion">BRANDY<br>INFUSED WITH<br>NAARTJIES</p>
      <p class="volume">750ML</p>
    </section>
  </main>
</body>
</html>
```